Google Form Graphic to suit our Brand and industry

Create a graphic / image for us to put at the top of our client enquiry google form.
The image will be a section of an architectural home with our branding over the top. Preferably translucent.
The image must suit the shape of the google forms image, which is an elongated rectangle
#003d5d - brand colour

Target Market(s)

residential home owners, high end architectural homes

Industry/Entity Type

Residential construction

Colors
0054AA
0677BA
7BADD7
CADEEF
E8F1F8

Requirements
Must have
• our branding and a photo of an architectural home in the background

```html
<!DOCTYPE html>
<html lang="en">
<head>
<meta charset="utf-8">
<title>Vero Buildworks – Form Header Options</title>
<link href="https://fonts.googleapis.com/css2?family=Poppins:wght@400;500&display=swap" rel="stylesheet">
<style>
  :root {
    --page-bg: #ffffff;
    --label-ink: #1a1a1a;
    --brand-blue: #0a6aa3;
    --brand-deep: #003d5d;
    --wordmark: #ffffff;
    --sky-top: #b9b4b2;
    --sky-warm: #d9c2b2;
    --timber: #7a5138;
    --timber-dark: #3f2a1e;
    --foliage: #4d5a35;
  }
  * { margin: 0; padding: 0; box-sizing: border-box; }
  html, body {
    width: 1200px; height: 1114px; overflow: hidden;
    background: var(--page-bg);
    font-family: "Poppins", sans-serif;
  }
  .sheet { position: relative; width: 1200px; height: 1114px; }
  .option-label {
    position: absolute; left: 197px;
    font-size: 11px; font-weight: 400; letter-spacing: 3.4px;
    color: var(--label-ink);
  }
  .banner {
    position: absolute; left: 198px; width: 824px; height: 207px;
    overflow: hidden;
  }
  .banner-photo {
    position: absolute; inset: 0;
    background:
      radial-gradient(ellipse 40% 55% at 92% 40%, var(--foliage) 0%, transparent 70%),
      linear-gradient(180deg, transparent 0%, transparent 30%, rgba(63,42,30,0.85) 70%, var(--timber-dark) 100%),
      linear-gradient(100deg, var(--sky-top) 0%, var(--sky-warm) 45%, var(--timber) 65%, var(--foliage) 100%);
  }
  .banner-overlay { position: absolute; inset: 0; width: 100%; height: 100%; }
  .banner-overlay polygon { fill: var(--brand-blue); opacity: 0.88; }
  .wordmark {
    position: absolute; color: var(--wordmark);
    font-weight: 500; white-space: nowrap; line-height: 1;
  }
  .label-a { top: 88px; }
  .label-b { top: 444px; }
  .label-c { top: 800px; }
  .banner-a { top: 117px; }
  .banner-b { top: 471px; }
  .banner-c { top: 831px; }
  .banner-a .wordmark { left: 95px; top: 96px; font-size: 24px; letter-spacing: 7px; }
  .banner-b .wordmark { left: 120px; top: 86px; font-size: 36px; letter-spacing: 11px; }
  .banner-c .wordmark { left: 122px; top: 78px; font-size: 48px; letter-spacing: 14px; }
</style>
</head>
<body>
<div class="sheet">
  <p class="option-label label-a">OPTIONS A</p>
  <div class="banner banner-a">
    <div class="banner-photo" role="img" aria-label="Photo of a modern timber architectural home with large glass windows among trees at dusk"></div>
    <svg class="banner-overlay" viewBox="0 0 824 207" preserveAspectRatio="none" aria-hidden="true">
      <polygon points="0,0 266,0 187,110 271,207 0,207"/>
    </svg>
    <span class="wordmark">VERO BUILDWORKS</span>
  </div>

  <p class="option-label label-b">OPTIONS B</p>
  <div class="banner banner-b">
    <div class="banner-photo" role="img" aria-label="Photo of a modern timber architectural home with large glass windows among trees at dusk"></div>
    <svg class="banner-overlay" viewBox="0 0 824 207" preserveAspectRatio="none" aria-hidden="true">
      <polygon points="0,0 345,0 274,108 346,207 0,207"/>
    </svg>
    <span class="wordmark">VERO BUILDWORKS</span>
  </div>

  <p class="option-label label-c">OPTIONS C</p>
  <div class="banner banner-c">
    <div class="banner-photo" role="img" aria-label="Photo of a modern timber architectural home with large glass windows among trees at dusk"></div>
    <svg class="banner-overlay" viewBox="0 0 824 207" preserveAspectRatio="none" aria-hidden="true">
      <polygon points="0,0 381,0 316,102 384,207 0,207"/>
    </svg>
    <span class="wordmark">VERO BUILDWORKS</span>
  </div>
</div>
</body>
</html>
```